tavish lumen brochure

double sided 3 fold brochure - old brochure and text is shown - keep the same text but i'd like a new layout and colors and maybe a new logo

```html
<!DOCTYPE html>
<html lang="en">
<head>
<meta charset="UTF-8">
<title>Tavish Lumen — Brochure Inside Spread</title>
<link rel="stylesheet" href="https://fonts.googleapis.com/css2?family=Alegreya:ital,wght@0,500;0,700;1,500&family=Alegreya+Sans:ital,wght@0,400;0,500;0,700;1,400;1,500&display=swap">
<style>
  :root {
    --cream: #f8f2e9;
    --sand: #efe3d1;
    --teal: #1e4b57;
    --teal-soft: #2c6170;
    --plum: #5a2b6b;
    --coral: #e06f4c;
    --ink: #2a2437;
    --ink-soft: #4a4257;
    --on-dark: #f3ede4;
    --on-dark-soft: #c9dde1;
  }
  * { margin: 0; padding: 0; box-sizing: border-box; }
  html, body { width: 1200px; height: 933px; overflow: hidden; background: var(--cream); }
  .spread {
    display: flex;
    width: 1200px;
    height: 933px;
    font-family: "Alegreya Sans", sans-serif;
    font-size: 13.5px;
    line-height: 19.5px;
    color: var(--ink);
  }
  .panel {
    position: relative;
    width: 400px;
    height: 933px;
    padding: 58px 36px 40px;
  }
  .panel::before {
    content: "";
    position: absolute;
    left: 36px; top: 30px;
    width: 48px; height: 4px;
    background: var(--coral);
    border-radius: 2px;
  }
  .panel--intro { background: var(--cream); }
  .panel--method { background: var(--teal); color: var(--on-dark); }
  .panel--voices { background: var(--sand); }

  .section-title {
    font-family: "Alegreya", serif;
    font-weight: 700;
    font-size: 28px;
    line-height: 32px;
    color: var(--plum);
    margin-bottom: 18px;
  }
  .panel--method .section-title { color: var(--on-dark); }

  .lead p { margin-bottom: 9px; }
  .panel--intro .lead p:first-child {
    font-size: 15px;
    line-height: 22px;
    color: var(--ink);
  }

  .sub-title {
    font-family: "Alegreya", serif;
    font-style: italic;
    font-weight: 500;
    font-size: 17px;
    line-height: 22px;
    color: var(--coral);
    margin-bottom: 10px;
  }

  .benefits {
    margin-top: 22px;
    padding-top: 18px;
    border-top: 1px solid rgba(90, 43, 107, 0.25);
  }
  .benefit-list { list-style: none; }
  .benefit-list li {
    position: relative;
    padding-left: 18px;
    margin-bottom: 8px;
    color: var(--ink-soft);
  }
  .benefit-list li::before {
    content: "";
    position: absolute;
    left: 0; top: 7px;
    width: 7px; height: 7px;
    border-radius: 50%;
    background: var(--coral);
  }

  .panel--method .lead p { color: var(--on-dark-soft); margin-bottom: 10px; }
  .panel--method .lead p:first-child { color: var(--on-dark); }

  .testimonial {
    background: var(--cream);
    border-left: 4px solid var(--plum);
    border-radius: 0 6px 6px 0;
    padding: 14px 16px 12px;
    margin-bottom: 16px;
  }
  .testimonial .sub-title { color: var(--plum); font-size: 16px; margin-bottom: 6px; }
  .testimonial p { margin-bottom: 8px; color: var(--ink-soft); }
  .testimonial p:last-of-type { margin-bottom: 6px; }
  .signature {
    display: block;
    font-weight: 700;
    font-size: 12px;
    letter-spacing: 0.08em;
    text-transform: uppercase;
    color: var(--coral);
  }
</style>
</head>
<body>
<main class="spread">
  <section class="panel panel--intro">
    <h2 class="section-title">Tavish Lumen</h2>
    <div class="lead">
      <p>Tavish Lumen is the amazing phenomenon of a hidden language that is imbedded backwards into the sounds of our speech. If human speech is recorded and played backwards, words and sentences can be heard that relate directly to what is being spoken forwards. These backward phrases detail our deepest thoughts, and hidden truths and feelings from the depths of the unconscious mind.</p>
    </div>
    <div class="benefits">
      <h3 class="sub-title">How can you benefit from Tavish Lumen?</h3>
      <ul class="benefit-list">
        <li>Discover causes of negative behavior patterns and restructure them into positive, powerful aspects of the self, allowing you to function at your fullest potential.</li>
        <li>Empower your business decisions and align your goals to your own inner truth and direction.</li>
        <li>Improve relationships by identifying and changing deep-seated issues that may be hampering trust, openness and sharing.</li>
        <li>Help your children overcome personal, physical or educational difficulties so that they may enjoy life and develop more fully.</li>
        <li>Gain insight into physical conditions to support and enable more complete healing.</li>
        <li>Access your Higher Self, Truest Truth, Soul Purpose.</li>
      </ul>
    </div>
  </section>

  <section class="panel panel--method">
    <h2 class="section-title">How it works</h2>
    <div class="lead">
      <p>The backward messages are received and understood by the human mind and there are many instances of entire reversed conversations where questions are asked and answers subsequently given, all in reverse. This may explain the many aspects of human intuition. In fact children speak backwards before they speak forwards, with single words being detected as early as four months, then, as forward speech begins, the two modes of speech gradually combine into one, forming an overall bi-level communication process.</p>
      <p>The unconscious mind holds knowledge and memory of all we have experienced and is the main motivator for most of our thoughts, beliefs and actions, even when they are not fully understood by the conscious mind. By accessing this wealth of information, using Tavish Lumen, it is possible to find where negative experiences or beliefs, usually depicted in metaphors or pictures, may be creating behaviors that are troublesome or bewildering.</p>
      <p>Behavioral change is then achieved by altering the unconscious metaphors. This is accomplished by using a series of unique guided visualization journeys called Innerpaths, which are based on information from the individuals’ reversals. As the pictures or metaphors are changed with this process, so too do unconscious behaviors and life outcomes also change.</p>
    </div>
  </section>

  <section class="panel panel--voices">
    <h2 class="section-title">Testimonials</h2>
    <article class="testimonial">
      <h3 class="sub-title">Personal testimonial</h3>
      <p>Truly an amazing journey and the results are life changing. What seemed like a hopeless situation is now a life full of love, respect, honesty and warmth, all this due to Tavish Lumen and the guidance, compassion and dedication of Miles Dorran.</p>
      <span class="signature">G. Pellarini, NSW</span>
    </article>
    <article class="testimonial">
      <h3 class="sub-title">Business testimonial</h3>
      <p>I needed help with finances and couldn’t seem to get it together with money. If you took all my cash assets and business liabilities, there was a major shortfall. I was surviving very basically on business turnover. Miles and I did some reversals and trance work.</p>
      <p>Six months later, I have reduced that shortfall by 75%, my business now turns over 100k a month, I own an airplane I paid cash for, I have had two great holidays and am off to America in November. I now buy good clothes, food and goods and really live well. It is impossible to reverse time and try all this without Miles’s help. However, if I could I am sure things would not be quite so abundant! Sometime soon, I would like to consider some more reversals.</p>
      <span class="signature">R. Whitcombe, Tasmania</span>
    </article>
  </section>
</main>
</body>
</html>
```